Adult Flushable Wipes Product Packaging design

We are launching an adult flushable wipe and we require a logo & product packaging design.

The brand is called: Velvet Steward

The wipe will be slightly upmarket and will sell mainly online. The branding should be funny but still professional. It's intended audience is men between 18-45 and it will be used as a body cleansing wipe.

for general body cleaning
-bathroom/toilet wipes
-grooming wipes
-refreshing wipes

Target Market(s)

Men Ages 18-45

Font styles to use
Decorative

Colors
86cfc6
33b8a4
85cae6
33a6d7

Requirements
Must have
• there are 50 wipes per pack. this should be incorporated in the design.
• the wipes are 5.9" x 7.9" this should be incorporated in the design.
• the wipes have a fragrance which we will call the "Velvet Breeze" this should be incorporated in the design.
Nice to have
• We like the idea of incorporating a butler/tuxedo into the product design. lots of black/white with a matte finish and can also have some silver.
Should not have
• too many colours. we want a simple design

```html
<!DOCTYPE html>
<html lang="en">
<head>
<meta charset="utf-8">
<title>Velvet Steward – Wipe Pack Colour Options</title>
<link rel="stylesheet" href="https://fonts.googleapis.com/css2?family=Anton&family=Raleway:wght@400;500&family=Roboto+Condensed:wght@400;700;900&display=swap">
<style>
  :root{
    --ink:#111111;
    --seal:#e4e6ea;
    --blue:#2a92be;
    --blue-light:#4fa9cf;
    --teal:#29a08b;
    --teal-light:#48b3a0;
    --label:#1a1a1a;
  }
  *{box-sizing:border-box;margin:0;padding:0}
  html,body{width:1200px;height:884px;overflow:hidden}
  body{background:linear-gradient(#f4f4f4,#e6e6e6);position:relative;font-family:"Raleway",sans-serif}

  .pack{position:absolute;top:99px;width:498px;height:687px;color:#fff}
  .pack--blue{left:86px;--brand:var(--blue);--brand-light:var(--blue-light)}
  .pack--teal{left:609px;--brand:var(--teal);--brand-light:var(--teal-light)}
  .pack__shape{position:absolute;inset:0}

  .pack__maker{position:absolute;left:150px;top:30px;width:198px;text-align:center;
    font-family:"Anton",sans-serif;font-size:17px;letter-spacing:1px;color:var(--ink);text-transform:uppercase}

  .pack__splash{position:absolute;left:425px;top:62px;width:66px;height:140px;
    background:radial-gradient(ellipse at 60% 50%,rgba(120,180,220,.55),rgba(200,225,240,0) 70%)}

  .pack__title{position:absolute;left:0;top:0;width:498px;height:300px}

  .copy{position:absolute;left:49px;width:252px}
  .copy h2{font-weight:400;font-size:14.5px;letter-spacing:.3px;margin-bottom:6px}
  .copy p{font-size:7.6px;line-height:10.4px;letter-spacing:-.1px;opacity:.95}
  .copy--intro{top:321px}
  .copy--made{top:415px}
  .copy--ingredients{top:472px}

  .facts{position:absolute;left:321px;top:305px;width:130px;height:219px;background:#fff;
    border:1px solid var(--ink);outline:1px solid #fff;color:var(--ink);overflow:hidden;
    font-family:"Roboto Condensed",sans-serif;padding:2px 4px;font-size:8.2px;line-height:9.6px}
  .facts__head{font-weight:900;font-size:15.5px;line-height:17px;letter-spacing:-.2px}
  .facts__rule{border-top:4px solid var(--ink);margin:2px 0 1px}
  .facts__rule--thin{border-top-width:1px}
  .facts__row{display:flex;justify-content:space-between;border-bottom:1px solid var(--ink);padding:1px 0}
  .facts__row b{font-weight:700}
  .facts__row--indent{padding-left:10px}
  .facts__small{font-size:6.4px;line-height:7.6px;padding-top:1px}
  .facts__note{font-size:5.9px;line-height:7px;border-top:1px solid var(--ink);margin-top:2px;padding-top:1px;letter-spacing:-.1px}
  .facts__right{text-align:right;font-size:7.2px;font-weight:700}

  .band{position:absolute;left:11px;top:547px;width:477px;height:41px;background:var(--ink);
    display:flex;align-items:center;padding:0 25px 0 36px;color:#fff}
  .band__made{font-size:8.8px;line-height:11px;width:188px;letter-spacing:.2px}
  .band__size{font-size:15px;letter-spacing:.3px;width:180px}
  .band__marks{margin-left:auto;display:flex;gap:6px}

  .benefits{position:absolute;left:11px;top:600px;width:477px;display:flex}
  .benefit{width:91px;text-align:center;font-weight:500;font-size:8.5px;line-height:10px;color:#eef8fb}
  .benefit svg{display:block;margin:0 auto 4px}

  .badge{position:absolute;left:390px;top:599px;width:70px;height:70px;border-radius:50%;background:#222;
    display:flex;flex-direction:column;align-items:center;justify-content:center;font-family:"Anton",sans-serif;font-size:15px;line-height:16px}
  .badge__count{color:var(--brand-light)}
  .badge__unit{color:#fff}

  .option-label{position:absolute;top:818px;font-family:"Anton",sans-serif;font-size:34px;letter-spacing:.5px;color:var(--label);transform:translateX(-50%)}
</style>
</head>
<body>

<!-- Pack, blue variant -->
<section class="pack pack--blue">
  <svg class="pack__shape" viewBox="0 0 498 687" aria-hidden="true">
    <defs>
      <linearGradient id="paperBlue" x1="0" y1="0" x2="0" y2="1"><stop offset="0" stop-color="#ffffff"/><stop offset="1" stop-color="#dfe2e6"/></linearGradient>
    </defs>
    <rect x="0" y="4" width="498" height="44" fill="var(--seal)"/>
    <path d="M0 4 l6 -4 l6 4 l6 -4 l6 4 l6 -4 l6 4 l6 -4 l6 4 l6 -4 l6 4 l6 -4 l6 4 l6 -4 l6 4 l6 -4 l6 4 l6 -4 l6 4 l6 -4 l6 4 l6 -4 l6 4 l6 -4 l6 4 l6 -4 l6 4 l6 -4 l6 4 l6 -4 l6 4 l6 -4 l6 4 l6 -4 l6 4 l6 -4 l6 4 l6 -4 l6 4 l6 -4 l6 4 l6 -4 l6 4 l6 -4 l6 4 l6 -4 l6 4 l6 -4 l6 4 l6 -4 l6 4 l6 -4 l6 4 l6 -4 l6 4 l6 -4 l6 4 l6 -4 l6 4 l6 -4 l6 4 l6 -4 l6 4 l6 -4 l6 4 l6 -4 l6 4 l6 -4 l6 4 l6 -4 l6 4 l6 -4 l6 4 l6 -4 l6 4 l6 -4 l6 4 l6 -4 l6 4 l6 -4 l6 4 l6 -4 l6 4 l6 -4 l6 4 L498 4 Z" fill="var(--seal)"/>
    <rect x="11" y="48" width="477" height="260" fill="url(#paperBlue)"/>
    <polygon points="11,297 488,254 488,650 11,650" fill="var(--brand)"/>
    <rect x="0" y="588" width="498" height="95" fill="var(--brand-light)"/>
    <path d="M0 683 l6 4 l6 -4 l6 4 l6 -4 l6 4 l6 -4 l6 4 l6 -4 l6 4 l6 -4 l6 4 l6 -4 l6 4 l6 -4 l6 4 l6 -4 l6 4 l6 -4 l6 4 l6 -4 l6 4 l6 -4 l6 4 l6 -4 l6 4 l6 -4 l6 4 l6 -4 l6 4 l6 -4 l6 4 l6 -4 l6 4 l6 -4 l6 4 l6 -4 l6 4 l6 -4 l6 4 l6 -4 l6 4 l6 -4 l6 4 l6 -4 l6 4 l6 -4 l6 4 l6 -4 l6 4 l6 -4 l6 4 l6 -4 l6 4 l6 -4 l6 4 l6 -4 l6 4 l6 -4 l6 4 l6 -4 l6 4 l6 -4 l6 4 l6 -4 l6 4 l6 -4 l6 4 l6 -4 l6 4 l6 -4 l6 4 l6 -4 l6 4 l6 -4 l6 4 l6 -4 l6 4 l6 -4 l6 4 l6 -4 l6 4 l6 -4 l6 4 l6 -4 l6 4 l6 -4 L498 683 Z" fill="var(--brand-light)"/>
    <g stroke="#ffffff" stroke-opacity=".5" stroke-width="1"><line x1="0" y1="14" x2="498" y2="14"/><line x1="0" y1="24" x2="498" y2="24"/><line x1="0" y1="34" x2="498" y2="34"/><line x1="0" y1="660" x2="498" y2="660"/><line x1="0" y1="670" x2="498" y2="670"/></g>
  </svg>

  <div class="pack__maker">Velvet Steward</div>
  <div class="pack__splash" role="img" aria-label="Water splash illustration"></div>

  <svg class="pack__title" viewBox="0 0 498 300" aria-label="Velvet Steward">
    <text x="76" y="172" font-family="Anton, sans-serif" font-size="66" fill="var(--ink)" textLength="262" lengthAdjust="spacingAndGlyphs">VELVET</text>
    <text x="76" y="270" font-family="Anton, sans-serif" font-size="104" fill="var(--brand)" textLength="360" lengthAdjust="spacingAndGlyphs">STEWARD</text>
  </svg>

  <div class="copy copy--intro">
    <h2>Comfortable wipe</h2>
    <p>Wet wipe for cleaning hands and body with antibacterial effectiveness. Soft, environmental and skin friendly, alcohol free, premium wipe with our Velvet Breeze fragrance. Widely used in cars, at home, in restaurants, in beach bars, on the beach, on campsites, during and after golf and in airplanes. Customers love the softness and are creative how to use them. Be careful, you'll get addicted.</p>
  </div>
  <div class="copy copy--made">
    <h2>Smart wipes</h2>
    <p>Made in the EU, designed by Velvet Steward BV, P.O. Box 4182, 3512AB Utrecht - The Netherlands www.velvetsteward-shop.com</p>
  </div>
  <div class="copy copy--ingredients">
    <h2>Ingredients</h2>
    <p>Aqua, Decyl Glucoside, Citrus Reticulate Fruit Extract, Glycerin, Sodium Caproyl/Lauroyl Lactylate, Triethyl Citrate, Parfum, Sodium Benzoate, Potassium Sorbate, Citric Acid.</p>
  </div>

  <div class="facts">
    <div class="facts__head">Nutrition Facts</div>
    <div>Serving Size 1 pouch (23g)</div>
    <div>Servings Per Container 5</div>
    <div class="facts__rule"></div>
    <div class="facts__row"><b>Amount Per Serving</b></div>
    <div class="facts__row"><span><b>Calories</b> 70</span></div>
    <div class="facts__rule facts__rule--thin"></div>
    <div class="facts__right">% Daily Value*</div>
    <div class="facts__row"><span><b>Total Fat</b> 0g</span><b>0%</b></div>
    <div class="facts__row"><span><b>Sodium</b> 55mg</span><b>2%</b></div>
    <div class="facts__row"><span><b>Total Carb.</b> 19g</span><b>6%</b></div>
    <div class="facts__row facts__row--indent"><span>Sugars 11g</span></div>
    <div class="facts__row"><span><b>Protein</b> 0g</span></div>
    <div class="facts__rule"></div>
    <div class="facts__row"><span>Vitamin C 100%</span></div>
    <div class="facts__small">Not a significant source of calories from fat, saturated fat, trans fat, cholesterol, dietary fiber, vitamin A, calcium and iron.</div>
    <div class="facts__note">*Percent Daily Values are based on a 2,000 calorie diet.</div>
  </div>

  <div class="band">
    <div class="band__made">MADE IN THE EU,<br>DESIGNED BY VELVET STEWARD</div>
    <div class="band__size">SIZE: 5.9" X 7.9"</div>
    <div class="band__marks" aria-label="Recycling marks">
      <svg width="20" height="20" viewBox="0 0 20 20"><circle cx="10" cy="10" r="9" fill="#fff"/><path d="M5 10 a5 5 0 0 1 9 -3 M15 10 a5 5 0 0 1 -9 3" stroke="#111" stroke-width="2" fill="none"/></svg>
      <svg width="16" height="20" viewBox="0 0 16 20"><circle cx="11" cy="3" r="2" fill="#fff"/><path d="M2 8 h9 l-1 11 h-7 z" fill="none" stroke="#fff" stroke-width="1.6"/><path d="M10 6 l4 6" stroke="#fff" stroke-width="1.6"/></svg>
    </div>
  </div>

  <div class="benefits">
    <div class="benefit"><svg width="24" height="26" viewBox="0 0 24 26"><path d="M18 2 L12 14" stroke="#fff" stroke-width="2"/><path d="M8 12 l8 4 l-6 8 l-6 -3 z" fill="#fff"/></svg>Deep<br>Cleansing</div>
    <div class="benefit"><svg width="24" height="26" viewBox="0 0 24 26"><path d="M4 20 C8 14 10 10 14 4 M10 14 c4 0 8 2 10 6 M14 4 l2 8" stroke="#fff" stroke-width="1.6" fill="none"/></svg>Promotes<br>Healthy Skin</div>
    <div class="benefit"><svg width="24" height="26" viewBox="0 0 24 26"><circle cx="12" cy="13" r="8" fill="none" stroke="#fff" stroke-width="4" stroke-dasharray="3 2.3"/><circle cx="12" cy="13" r="5" fill="#fff"/></svg>Anti-bacterial<br>Wipes</div>
    <div class="benefit"><svg width="30" height="26" viewBox="0 0 30 26"><path d="M2 22 L16 12 L28 22 Z" fill="none" stroke="#fff" stroke-width="1.5"/><circle cx="10" cy="18" r="2" fill="#fff"/><circle cx="15" cy="16" r="2" fill="#fff"/><circle cx="19" cy="19" r="2" fill="#fff"/><circle cx="13" cy="8" r="1.2" fill="#fff"/><circle cx="17" cy="7" r="1.2" fill="#fff"/></svg>Gently Remove<br>Impurities</div>
  </div>
  <div class="badge"><span class="badge__count">50 WIPES</span><span class="badge__unit">PER PACK</span></div>
</section>

<!-- Pack, teal variant -->
<section class="pack pack--teal">
  <svg class="pack__shape" viewBox="0 0 498 687" aria-hidden="true">
    <defs>
      <linearGradient id="paperTeal" x1="0" y1="0" x2="0" y2="1"><stop offset="0" stop-color="#ffffff"/><stop offset="1" stop-color="#dfe2e6"/></linearGradient>
    </defs>
    <rect x="0" y="4" width="498" height="44" fill="var(--seal)"/>
    <path d="M0 4 l6 -4 l6 4 l6 -4 l6 4 l6 -4 l6 4 l6 -4 l6 4 l6 -4 l6 4 l6 -4 l6 4 l6 -4 l6 4 l6 -4 l6 4 l6 -4 l6 4 l6 -4 l6 4 l6 -4 l6 4 l6 -4 l6 4 l6 -4 l6 4 l6 -4 l6 4 l6 -4 l6 4 l6 -4 l6 4 l6 -4 l6 4 l6 -4 l6 4 l6 -4 l6 4 l6 -4 l6 4 l6 -4 l6 4 l6 -4 l6 4 l6 -4 l6 4 l6 -4 l6 4 l6 -4 l6 4 l6 -4 l6 4 l6 -4 l6 4 l6 -4 l6 4 l6 -4 l6 4 l6 -4 l6 4 l6 -4 l6 4 l6 -4 l6 4 l6 -4 l6 4 l6 -4 l6 4 l6 -4 l6 4 l6 -4 l6 4 l6 -4 l6 4 l6 -4 l6 4 l6 -4 l6 4 l6 -4 l6 4 l6 -4 l6 4 l6 -4 l6 4 l6 -4 l6 4 l6 -4 l6 4 L498 4 Z" fill="var(--seal)"/>
    <rect x="11" y="48" width="477" height="260" fill="url(#paperTeal)"/>
    <polygon points="11,297 488,254 488,650 11,650" fill="var(--brand)"/>
    <rect x="0" y="588" width="498" height="95" fill="var(--brand-light)"/>
    <path d="M0 683 l6 4 l6 -4 l6 4 l6 -4 l6 4 l6 -4 l6 4 l6 -4 l6 4 l6 -4 l6 4 l6 -4 l6 4 l6 -4 l6 4 l6 -4 l6 4 l6 -4 l6 4 l6 -4 l6 4 l6 -4 l6 4 l6 -4 l6 4 l6 -4 l6 4 l6 -4 l6 4 l6 -4 l6 4 l6 -4 l6 4 l6 -4 l6 4 l6 -4 l6 4 l6 -4 l6 4 l6 -4 l6 4 l6 -4 l6 4 l6 -4 l6 4 l6 -4 l6 4 l6 -4 l6 4 l6 -4 l6 4 l6 -4 l6 4 l6 -4 l6 4 l6 -4 l6 4 l6 -4 l6 4 l6 -4 l6 4 l6 -4 l6 4 l6 -4 l6 4 l6 -4 l6 4 l6 -4 l6 4 l6 -4 l6 4 l6 -4 l6 4 l6 -4 l6 4 l6 -4 l6 4 l6 -4 l6 4 l6 -4 l6 4 l6 -4 l6 4 l6 -4 l6 4 l6 -4 l6 4 l6 -4 l6 4 l6 -4 L498 683 Z" fill="var(--brand-light)"/>
    <g stroke="#ffffff" stroke-opacity=".5" stroke-width="1"><line x1="0" y1="14" x2="498" y2="14"/><line x1="0" y1="24" x2="498" y2="24"/><line x1="0" y1="34" x2="498" y2="34"/><line x1="0" y1="660" x2="498" y2="660"/><line x1="0" y1="670" x2="498" y2="670"/></g>
  </svg>

  <div class="pack__maker">Velvet Steward</div>
  <div class="pack__splash" role="img" aria-label="Water splash illustration"></div>

  <svg class="pack__title" viewBox="0 0 498 300" aria-label="Velvet Steward">
    <text x="76" y="172" font-family="Anton, sans-serif" font-size="66" fill="var(--ink)" textLength="262" lengthAdjust="spacingAndGlyphs">VELVET</text>
    <text x="76" y="270" font-family="Anton, sans-serif" font-size="104" fill="var(--brand)" textLength="360" lengthAdjust="spacingAndGlyphs">STEWARD</text>
  </svg>

  <div class="copy copy--intro">
    <h2>Comfortable wipe</h2>
    <p>Wet wipe for cleaning hands and body with antibacterial effectiveness. Soft, environmental and skin friendly, alcohol free, premium wipe with our Velvet Breeze fragrance. Widely used in cars, at home, in restaurants, in beach bars, on the beach, on campsites, during and after golf and in airplanes. Customers love the softness and are creative how to use them. Be careful, you'll get addicted.</p>
  </div>
  <div class="copy copy--made">
    <h2>Smart wipes</h2>
    <p>Made in the EU, designed by Velvet Steward BV, P.O. Box 4182, 3512AB Utrecht - The Netherlands www.velvetsteward-shop.com</p>
  </div>
  <div class="copy copy--ingredients">
    <h2>Ingredients</h2>
    <p>Aqua, Decyl Glucoside, Citrus Reticulate Fruit Extract, Glycerin, Sodium Caproyl/Lauroyl Lactylate, Triethyl Citrate, Parfum, Sodium Benzoate, Potassium Sorbate, Citric Acid.</p>
  </div>

  <div class="facts">
    <div class="facts__head">Nutrition Facts</div>
    <div>Serving Size 1 pouch (23g)</div>
    <div>Servings Per Container 5</div>
    <div class="facts__rule"></div>
    <div class="facts__row"><b>Amount Per Serving</b></div>
    <div class="facts__row"><span><b>Calories</b> 70</span></div>
    <div class="facts__rule facts__rule--thin"></div>
    <div class="facts__right">% Daily Value*</div>
    <div class="facts__row"><span><b>Total Fat</b> 0g</span><b>0%</b></div>
    <div class="facts__row"><span><b>Sodium</b> 55mg</span><b>2%</b></div>
    <div class="facts__row"><span><b>Total Carb.</b> 19g</span><b>6%</b></div>
    <div class="facts__row facts__row--indent"><span>Sugars 11g</span></div>
    <div class="facts__row"><span><b>Protein</b> 0g</span></div>
    <div class="facts__rule"></div>
    <div class="facts__row"><span>Vitamin C 100%</span></div>
    <div class="facts__small">Not a significant source of calories from fat, saturated fat, trans fat, cholesterol, dietary fiber, vitamin A, calcium and iron.</div>
    <div class="facts__note">*Percent Daily Values are based on a 2,000 calorie diet.</div>
  </div>

  <div class="band">
    <div class="band__made">MADE IN THE EU,<br>DESIGNED BY VELVET STEWARD</div>
    <div class="band__size">SIZE: 5.9" X 7.9"</div>
    <div class="band__marks" aria-label="Recycling marks">
      <svg width="20" height="20" viewBox="0 0 20 20"><circle cx="10" cy="10" r="9" fill="#fff"/><path d="M5 10 a5 5 0 0 1 9 -3 M15 10 a5 5 0 0 1 -9 3" stroke="#111" stroke-width="2" fill="none"/></svg>
      <svg width="16" height="20" viewBox="0 0 16 20"><circle cx="11" cy="3" r="2" fill="#fff"/><path d="M2 8 h9 l-1 11 h-7 z" fill="none" stroke="#fff" stroke-width="1.6"/><path d="M10 6 l4 6" stroke="#fff" stroke-width="1.6"/></svg>
    </div>
  </div>

  <div class="benefits">
    <div class="benefit"><svg width="24" height="26" viewBox="0 0 24 26"><path d="M18 2 L12 14" stroke="#fff" stroke-width="2"/><path d="M8 12 l8 4 l-6 8 l-6 -3 z" fill="#fff"/></svg>Deep<br>Cleansing</div>
    <div class="benefit"><svg width="24" height="26" viewBox="0 0 24 26"><path d="M4 20 C8 14 10 10 14 4 M10 14 c4 0 8 2 10 6 M14 4 l2 8" stroke="#fff" stroke-width="1.6" fill="none"/></svg>Promotes<br>Healthy Skin</div>
    <div class="benefit"><svg width="24" height="26" viewBox="0 0 24 26"><circle cx="12" cy="13" r="8" fill="none" stroke="#fff" stroke-width="4" stroke-dasharray="3 2.3"/><circle cx="12" cy="13" r="5" fill="#fff"/></svg>Anti-bacterial<br>Wipes</div>
    <div class="benefit"><svg width="30" height="26" viewBox="0 0 30 26"><path d="M2 22 L16 12 L28 22 Z" fill="none" stroke="#fff" stroke-width="1.5"/><circle cx="10" cy="18" r="2" fill="#fff"/><circle cx="15" cy="16" r="2" fill="#fff"/><circle cx="19" cy="19" r="2" fill="#fff"/><circle cx="13" cy="8" r="1.2" fill="#fff"/><circle cx="17" cy="7" r="1.2" fill="#fff"/></svg>Gently Remove<br>Impurities</div>
  </div>
  <div class="badge"><span class="badge__count">50 WIPES</span><span class="badge__unit">PER PACK</span></div>
</section>

<div class="option-label" style="left:332px">COLOR OPTION 1</div>
<div class="option-label" style="left:880px">COLOR OPTION 2</div>

</body>
</html>
```